website refresh with jungle and/or gorilla theme for marketing agency

Our marketing agency needs a creative website boost. The website (which is Wordpress) is:https://www.tallmoosestudio.com. Given our name, we would like to have a jungle/gorilla theme. The Moose website should have a beastly presence. See the site now and how the gorilla is in your face. The text can remain the same, we just need a new layout and/or graphics. What other direction can I give? Not sure, we will know it when we see it.

Target Market(s)

small and medium sized businesses

Industry/Entity Type

Digital Marketing

Number of Pages Required

1 page

Colors

Designer to choose colors to be used in the design.

Requirements
Must have
• I don't really have any must have's. I don't want to limit the creativity of the designer.
Nice to have
• I am encouraging an out of the box design, something that isn't so "boxy" and traditional like the other sites.
Should not have
• I don't like standard looking sites that have a boxy layout with your standard cartoon and/or basic icons.

```html
<!DOCTYPE html>
<html lang="en">
<head>
<meta charset="utf-8">
<title>Moose Marketing</title>
<link href="https://fonts.googleapis.com/css2?family=Poppins:wght@300;400;500;600;700&family=Libre+Baskerville:wght@400;700&display=swap" rel="stylesheet">
<style>
:root{
  --green:#2fb52f;
  --green-dark:#1d8f22;
  --blue:#2a7de1;
  --blue-deep:#1f6fd6;
  --teal:#1fc4d6;
  --ink:#222;
  --muted:#555;
  --grey-bg:#eeeeee;
  --white:#fff;
  --jungle-dark:#1f2a1c;
}
*{margin:0;padding:0;box-sizing:border-box}
html,body{width:1200px;height:4167px;overflow:hidden}
body{position:relative;font-family:'Poppins',sans-serif;color:var(--ink);background:var(--white)}
.abs{position:absolute}
/* header / hero */
.hero-wave{left:0;top:0}
.nav{right:58px;top:38px;display:flex;gap:28px;font-weight:600;font-size:19px}
.nav a{color:#111;text-decoration:none}
.nav a.active{color:var(--blue)}
.brand{left:92px;top:72px;width:180px;height:142px;background:rgba(255,255,255,.18);display:flex;flex-direction:column;align-items:center;justify-content:center;gap:4px;color:var(--white);font-weight:700}
.brand .big{font-size:44px;line-height:1}
.brand .small{font-size:22px;letter-spacing:2px}
.hero-title{left:143px;top:306px;color:var(--white);font-weight:700;font-size:36px;line-height:48px;width:440px}
.hero-sub{left:143px;top:413px;color:var(--white);font-weight:500;font-size:18px;line-height:26px;width:440px}
.btn-outline{left:143px;top:488px;width:150px;height:36px;border:2px solid var(--white);border-radius:18px;color:var(--white);font-size:14px;font-weight:600;display:flex;align-items:center;justify-content:center}
.hero-dots{left:315px;top:498px;display:flex;gap:8px;align-items:center}
.hero-dots span{width:11px;height:11px;border-radius:50%;background:var(--white)}
.hero-dots span.on{width:16px;height:16px;background:none;border:2px solid var(--white)}
.gorilla{border-radius:48% 42% 30% 30%;background:radial-gradient(ellipse at 50% 40%,#6a6a6a,#1a1a1a 70%)}
/* why */
.why-circle-a{left:40px;top:905px;width:240px;height:240px;border-radius:50%;background:#9ec8f7}
.why-circle-b{left:100px;top:1110px;width:180px;height:180px;border-radius:50%;background:#4fd3df}
.video{left:146px;top:882px;width:374px;height:374px;border-radius:50%;border:6px solid var(--white);background:radial-gradient(circle at 60% 60%,#6b5a4a,#2b2a29 75%);box-shadow:0 6px 20px rgba(0,0,0,.2);display:flex;align-items:center;justify-content:center}
.play{width:54px;height:54px;border-radius:50%;background:rgba(255,255,255,.9);display:flex;align-items:center;justify-content:center}
.why-title{left:566px;top:878px;font-size:46px;font-weight:400;color:#111;white-space:nowrap}
.why-title b{color:var(--blue);font-weight:600}
.why-block{left:567px;top:960px;width:490px;display:flex;flex-direction:column;align-items:flex-start}
.why-text{font-size:14px;line-height:27px;color:#333}
.why-text p+p{margin-top:12px}
.btn-blue{margin-top:22px;width:136px;height:40px;background:var(--blue);color:var(--white);font-size:14px;font-weight:600;display:flex;align-items:center;justify-content:center}
/* about */
.about-bg{left:0;top:1330px}
.about-title{left:0;width:1200px;top:1440px;text-align:center;font-size:52px;font-weight:400}
.about-title b{color:var(--blue);font-weight:600}
.about-text{left:190px;width:820px;top:1520px;text-align:center;font-size:14.5px;line-height:29px;color:#333}
.about-text p+p{margin-top:10px}
.card{top:1714px;width:295px;height:362px;background:var(--white);box-shadow:0 4px 16px rgba(0,0,0,.15);text-align:center;padding-top:34px}
.card .icon{width:98px;height:98px;border-radius:50%;margin:0 auto;background:linear-gradient(135deg,var(--teal),var(--blue));display:flex;align-items:center;justify-content:center}
.card h3{margin-top:32px;font-size:18px;font-weight:600}
.card p{margin:14px auto 0;width:230px;font-size:13.5px;line-height:24px;color:#444}
.card .more{margin:22px auto 0;width:104px;height:26px;border:2px solid var(--blue);border-radius:13px;font-size:11px;font-weight:600;color:var(--blue);display:flex;align-items:center;justify-content:center}
/* testimonial */
.jungle-band{left:0;top:2203px;width:1200px;height:672px;background:radial-gradient(ellipse at 30% 40%,#6fbf3a,#2f7d1f 55%,#14461a)}
.quote-frame{left:167px;top:2264px;width:888px;height:550px;background:rgba(255,255,255,.96);border:12px solid var(--white);display:flex;flex-direction:column;align-items:center;justify-content:center;padding:0 60px}
.quote-head{display:flex;align-items:center;gap:22px}
.avatar{width:120px;height:120px;border-radius:50%;background:linear-gradient(#9bb8d6,#6b7f91)}
.qmark{font-family:'Libre Baskerville',serif;font-size:64px;color:#aaa;line-height:1;margin-top:24px}
.quote-text{margin-top:22px;text-align:center;font-size:14.5px;line-height:30px;color:#333}
.quote-name{margin-top:12px;text-align:center;font-size:15px;color:var(--blue);font-weight:500}
.quote-dots{margin-top:22px;display:flex;gap:6px}
.quote-dots span{width:14px;height:14px;border-radius:50%;border:2px solid var(--blue)}
/* brands */
.brands-title{left:0;width:1200px;top:2985px;text-align:center;font-size:34px;font-weight:500}
.brand-row{left:170px;top:3090px;width:860px;display:flex;justify-content:space-between;align-items:center}
.brand-name{font-size:32px;font-weight:600;display:flex;align-items:center;gap:12px;white-space:nowrap}
/* quote form */
.map{left:139px;top:3315px;width:412px;height:363px;border-radius:8px;background:linear-gradient(135deg,#eef0e6,#d8e2ea);box-shadow:0 6px 20px rgba(0,0,0,.25);z-index:2}
.quote-box{left:306px;top:3281px;width:744px;height:433px;border-radius:10px;background:linear-gradient(160deg,#2f3f2c,var(--jungle-dark) 60%,#0f170f)}
.quote-title{left:776px;top:3325px;color:var(--white);font-size:34px;font-weight:700}
.field{left:611px;width:385px;height:38px;background:var(--white);font-size:13px;color:#666;padding:0 12px;display:flex;align-items:center}
.field.tall{align-items:flex-start;padding-top:12px;height:58px}
.submit{left:611px;top:3612px;width:385px;height:46px;background:var(--teal);color:var(--white);font-weight:600;font-size:17px;display:flex;align-items:center;justify-content:center}
/* footer */
.footer-wave{left:0;top:3560px}
.foot-h{top:3798px;color:var(--white);font-size:22px;font-weight:600}
.contact{left:144px;top:3862px;color:var(--white);font-size:13.5px;line-height:22px}
.contact .row{display:flex;gap:16px;margin-bottom:22px}
.signup-text{left:467px;top:3856px;width:330px;color:var(--white);font-size:12px;line-height:21px}
.email{left:467px;top:3922px;width:370px;height:40px;border-radius:20px;background:var(--white);font-size:12px;color:#777;padding-left:18px;display:flex;align-items:center}
.email b{position:absolute;right:0;top:0;height:40px;width:120px;border-radius:20px;background:#222;color:var(--white);font-size:12px;display:flex;align-items:center;justify-content:center}
.socials{left:476px;top:3986px;display:flex;gap:6px}
.socials span{width:24px;height:24px;border-radius:50%;border:1.5px solid var(--white)}
.links{left:909px;top:3850px;color:var(--white);font-size:14px;line-height:30px}
.foot-rule{left:118px;top:4062px;width:964px;height:1px;background:rgba(255,255,255,.35)}
.copyright{left:0;width:1200px;top:4110px;text-align:center;color:var(--white);font-size:13px}
</style>
</head>
<body>

<!-- hero -->
<svg class="abs hero-wave" width="1200" height="860" viewBox="0 0 1200 860" aria-hidden="true">
  <defs>
    <linearGradient id="heroGreen" x1="0" y1="0" x2="1" y2="1">
      <stop offset="0" stop-color="#3ec43a"/>
      <stop offset="1" stop-color="#1f9a25"/>
    </linearGradient>
  </defs>
  <path d="M0 0 H1200 V140 C1150 70 1080 0 980 20 C760 60 760 0 560 0 Z" fill="#ffffff"/>
  <path d="M0 0 H560 C700 0 760 40 880 30 C1000 20 1100 40 1200 150 V600 C1080 700 960 720 820 690 C640 650 520 760 340 720 C200 690 120 610 0 650 Z" fill="url(#heroGreen)"/>
  <path d="M0 650 C120 610 200 690 340 720 C520 760 640 650 820 690 C700 700 600 780 440 800 C260 820 120 740 0 760 Z" fill="#9be07a" opacity=".45"/>
</svg>
<nav class="abs nav"><a class="active">HOME</a><a>ABOUT</a><a>LEARN</a><a>PORTFOLIO</a><a>CONTACT</a></nav>
<div class="abs brand"><span class="big">Moose</span><span class="small">MARKETING</span></div>
<h1 class="abs hero-title">SOCIAL AND SEARCH MARKETING BEASTS</h1>
<p class="abs hero-sub">Get performance driven digital marketing leaders on your team</p>
<div class="abs btn-outline">READ MORE</div>
<div class="abs hero-dots"><span class="on"></span><span></span><span></span><span></span></div>
<div class="abs gorilla" style="left:600px;top:110px;width:540px;height:720px" role="img" aria-label="Large black and white photo of a gorilla leaning forward"></div>

<!-- why -->
<div class="abs why-circle-a"></div>
<div class="abs why-circle-b"></div>
<div class="abs video" role="img" aria-label="Video still of a presenter at a whiteboard">
  <div class="play"><svg width="20" height="22" viewBox="0 0 20 22"><path d="M3 2 L18 11 L3 20 Z" fill="#222"/></svg></div>
</div>
<h2 class="abs why-title">Why <b>Moose Marketing?</b></h2>
<div class="abs why-block">
  <div class="why-text">
    <p>Moose Marketing is the apex predator of the social and search marketing industries. We are senior marketing experts with the skills to create revenue-producing marketing funnels. In this age of big data, there is no better way to earn instant visibility with your audience than to have a REAL team of skilled pros on your side.</p>
    <p>Is your marketing funnel maximizing revenue and conversions? Learn the single biggest mistake companies make in their marketing funnel and how to fix it.</p>
  </div>
  <div class="btn-blue">READ MORE</div>
</div>

<!-- about -->
<svg class="abs about-bg" width="1200" height="880" viewBox="0 0 1200 880" aria-hidden="true">
  <path d="M0 60 C200 20 400 90 620 50 C820 15 1000 70 1200 40 V880 H0 Z" fill="#ececec"/>
</svg>
<div class="abs gorilla" style="left:916px;top:1240px;width:195px;height:260px" role="img" aria-label="Photo of a seated gorilla"></div>
<h2 class="abs about-title">About <b>Us</b></h2>
<div class="abs about-text">
  <p>What sets us apart from other marketing agencies is our team of A-players. Each team member has proven themselves to be in the top 1% of all marketers. They are the 1 percenters who are passionate about what they do and have proven experience to back up their incredible skill sets.</p>
  <p>Led by Daniel Harlow, who has built and sold 4 companies himself and written 5 books (one best-seller), the team at Moose Marketing specializes in user acquisition, lead generation, and brand visibility.</p>
</div>

<div class="abs card" style="left:147px">
  <div class="icon"><svg width="44" height="40" viewBox="0 0 44 40"><path d="M3 3 V37 H41" stroke="#fff" stroke-width="3" fill="none"/><rect x="10" y="20" width="5" height="13" fill="#fff"/><rect x="19" y="12" width="5" height="21" fill="#fff"/><rect x="28" y="16" width="5" height="17" fill="#fff"/></svg></div>
  <h3>GET MORE TRAFFIC</h3>
  <p>Sed ut perspiciatis unde omnis iste natus error sit voluptatem accusantium dmque laudantium, totam rem aperiam, eaque ipsa</p>
  <div class="more">READ MORE</div>
</div>
<div class="abs card" style="left:467px">
  <div class="icon"><svg width="50" height="36" viewBox="0 0 50 36"><circle cx="25" cy="10" r="7" fill="#fff"/><circle cx="10" cy="14" r="5" fill="#fff"/><circle cx="40" cy="14" r="5" fill="#fff"/><path d="M13 34 C13 22 37 22 37 34 Z" fill="#fff"/><path d="M1 34 C1 25 16 24 17 30 L15 34 Z M49 34 C49 25 34 24 33 30 L35 34 Z" fill="#fff"/></svg></div>
  <h3>HIGHER QUALITY LEADS</h3>
  <p>Sed ut perspiciatis unde omnis iste natus error sit voluptatem accusantium dmque laudantium, totam rem aperiam, eaque ipsa</p>
  <div class="more">READ MORE</div>
</div>
<div class="abs card" style="left:789px">
  <div class="icon"><svg width="44" height="40" viewBox="0 0 44 40"><rect x="3" y="3" width="38" height="34" fill="none" stroke="#fff" stroke-width="3"/><path d="M9 30 L18 20 L24 25 L35 12" stroke="#fff" stroke-width="3" fill="none"/><path d="M29 11 H36 V18" stroke="#fff" stroke-width="3" fill="none"/></svg></div>
  <h3>GET MORE SALES</h3>
  <p>Sed ut perspiciatis unde omnis iste natus error sit voluptatem accusantium dmque laudantium, totam rem aperiam, eaque ipsa</p>
  <div class="more">READ MORE</div>
</div>

<!-- testimonial -->
<div class="abs jungle-band" role="img" aria-label="Dense tropical leaves and yellow flowers"></div>
<div class="abs quote-frame">
  <div class="quote-head">
    <span class="qmark">&ldquo;</span>
    <div class="avatar" role="img" aria-label="Portrait photo of the client"></div>
    <span class="qmark">&rdquo;</span>
  </div>
  <p class="quote-text">For the same price of hiring one person in-house, I am a getting a team of senior marketers that constantly innovate and explore revenue opportunities. I highly recommend the team at Moose Marketing laudantium, totam rem aperiam, eaque ipsa quae ab illo inventore veritatis et quasi architecto beatae vitae dicta sunt explicabo. Nemo enim ipsam</p>
  <p class="quote-name">&mdash; Ronan Pike, Founder, Brightfold Goods</p>
  <div class="quote-dots"><span></span><span></span><span></span></div>
</div>

<!-- brands -->
<h2 class="abs brands-title">Name Brands We've Worked For</h2>
<div class="abs brand-row">
  <div class="brand-name" style="color:#111"><svg width="40" height="40"><circle cx="20" cy="20" r="18" fill="#2fae4a"/></svg>Crestline</div>
  <div class="brand-name" style="color:#b3202a">Weaverly Goods</div>
  <div class="brand-name" style="color:#1d3a7a">Harborpoint</div>
</div>

<!-- quote -->
<svg class="abs" style="left:0;top:3560px" width="1200" height="260" viewBox="0 0 1200 260" aria-hidden="true">
  <path d="M0 150 C80 120 180 150 240 190 V260 H0 Z" fill="var(--teal)"/>
</svg>
<div class="abs map" role="img" aria-label="Street map showing the office location"></div>
<div class="abs quote-box" role="img" aria-label="Dark jungle foliage backdrop"></div>
<h2 class="abs quote-title">GET A QUOTE</h2>
<div class="abs field" style="top:3390px">First name</div>
<div class="abs field" style="top:3440px">Email</div>
<div class="abs field" style="top:3490px">+1 &#9662;&nbsp;&nbsp; Phone</div>
<div class="abs field tall" style="top:3537px">How Can We Help?</div>
<div class="abs submit">SUBMIT</div>

<!-- footer -->
<svg class="abs footer-wave" width="1200" height="607" viewBox="0 0 1200 607" aria-hidden="true" style="z-index:-1">
  <path d="M0 220 C200 150 380 200 560 170 C760 130 920 60 1200 110 V607 H0 Z" fill="var(--blue-deep)"/>
</svg>
<h3 class="abs foot-h" style="left:144px">CONTACT US</h3>
<h3 class="abs foot-h" style="left:467px">SIGN UP TO RECEIVE EMAIL</h3>
<h3 class="abs foot-h" style="left:906px">QUICK LINKS</h3>
<div class="abs contact">
  <div class="row"><svg width="16" height="22" viewBox="0 0 16 22"><path d="M8 1 C3 1 1 5 1 8 C1 13 8 21 8 21 C8 21 15 13 15 8 C15 5 13 1 8 1 Z" fill="none" stroke="#fff" stroke-width="1.6"/><circle cx="8" cy="8" r="2.5" fill="#fff"/></svg><div>Moose Marketing<br>88 Cedar Hollow Rd, Ashford<br>CA 95010</div></div>
  <div class="row"><svg width="16" height="18" viewBox="0 0 16 18"><path d="M3 1 L6 1 L7 5 L5 7 C6 10 8 12 11 13 L13 11 L16 12 L16 15 C16 16 15 17 14 17 C7 17 1 10 1 3 C1 2 2 1 3 1 Z" fill="#fff"/></svg><div>Phone : 555-014-2290</div></div>
  <div class="row"><svg width="18" height="14" viewBox="0 0 18 14"><rect x="1" y="1" width="16" height="12" fill="none" stroke="#fff" stroke-width="1.5"/><path d="M1 1 L9 8 L17 1" fill="none" stroke="#fff" stroke-width="1.5"/></svg><div>Email : info@tallmoosestudio.com</div></div>
</div>
<p class="abs signup-text">Excepteur sint occaecat cupidatat non proident, sunt in culpa qui fermo enim ipsam voluptatem</p>
<div class="abs email">Enter Email<b>SUBSCRIBE</b></div>
<div class="abs socials"><span></span><span></span><span></span><span></span></div>
<div class="abs links">About<br>Learn<br>Portfolio<br>Contact<br>Privacy Policy<br>Terms &amp; Conditions</div>
<div class="abs foot-rule"></div>
<p class="abs copyright">Copyright &copy; Moose Marketing 2018. All rights reserved. | Privacy Policy</p>

</body>
</html>
```